Design a banner for a home page shop

I need someone who can design a banner for a photographic website.
The website has 2 main section shop and blog. You can advertize what u want. You can decide the images.

I need creative people.

I will pay the best one.

```html
<!DOCTYPE html>
<html lang="en">
<head>
<meta charset="UTF-8">
<title>Design Banner for Photography Website</title>
<link rel="stylesheet" href="https://fonts.googleapis.com/css2?family=Arimo:wght@400;700&display=swap">
<style>
  :root {
    --brand-red: #ff0010;
    --white: #ffffff;
    --ink: #111111;
    --slate-top: #36465c;
    --slate-bottom: #6f809a;
    --photo-dark: #2a2c30;
    --photo-mid: #8a8f98;
  }
  * { box-sizing: border-box; margin: 0; padding: 0; }
  html, body { width: 1200px; height: 605px; overflow: hidden; background: var(--white); }
  body { position: relative; font-family: "Arimo", Arial, sans-serif; color: var(--ink); }

  .header-band {
    position: absolute; left: 0; top: 0; width: 1200px; height: 89px;
    background: var(--brand-red);
    display: flex; align-items: center; justify-content: center;
  }
  .page-title {
    color: var(--white); font-weight: 700; font-size: 29px; letter-spacing: 0.3px;
  }

  .banner-label {
    position: absolute; top: 154px; font-weight: 700; font-size: 21px; letter-spacing: 0.3px;
  }
  .label-one { left: 109px; }
  .label-two { left: 641px; }

  .promo-banner {
    position: absolute; top: 205px; width: 506px; height: 267px;
    background: linear-gradient(180deg, var(--slate-top) 0%, var(--slate-bottom) 100%);
    color: var(--white);
  }
  .banner-one { left: 107px; }
  .banner-two { left: 641px; }

  .promo-heading {
    position: absolute; left: 12px; top: 30px; font-size: 27px; font-weight: 700; letter-spacing: 0.2px;
  }
  .promo-copy {
    position: absolute; left: 12px; top: 67px; font-size: 18.5px; line-height: 32px;
  }
  .promo-copy .lead { font-weight: 700; }

  .shop-button {
    position: absolute; left: 12px; top: 199px; width: 204px; height: 45px;
    background: var(--brand-red); display: flex; align-items: center;
    padding-left: 12px; gap: 8px; color: var(--white); font-size: 19px;
  }
  .shop-button .chevron { margin-left: 10px; }

  .product-photo {
    position: absolute; border-radius: 6px;
    background: radial-gradient(ellipse at 50% 45%, var(--photo-mid) 0%, var(--photo-dark) 85%);
    opacity: 0.9;
  }
  .photo-compact { left: 277px; top: 32px; width: 223px; height: 140px; }
  .photo-dslr { left: 336px; top: 35px; width: 156px; height: 157px; }

  .footer-band {
    position: absolute; left: 0; top: 548px; width: 1200px; height: 57px; background: var(--brand-red);
  }
</style>
</head>
<body>
  <header class="header-band">
    <h1 class="page-title">DESIGN BANNER FOR PHOTOGRAPHY WEBSITE</h1>
  </header>

  <h2 class="banner-label label-one">BANNER 01</h2>
  <h2 class="banner-label label-two">BANNER 02</h2>

  <section class="promo-banner banner-one">
    <div class="product-photo photo-compact" role="img" aria-label="Silver compact digital camera with wrist strap"></div>
    <h3 class="promo-heading">PHOTOGRAPHY</h3>
    <p class="promo-copy"><span class="lead">L</span>orem ipsum dolor sit amet, con-<br>sectetur adipiscing elit, sed do<br>eiusmod tempor incididunt ut<br>labore et dolore magna aliqua.</p>
    <div class="shop-button">
      <svg width="26" height="24" viewBox="0 0 26 24" fill="none" stroke="#fff" stroke-width="2" stroke-linejoin="round" stroke-linecap="round">
        <path d="M1 2h4l3 13h13l3-9H6.5"/>
        <path d="M9 7.5l1.5 6M13 7.5v6M17 7.5l-1.2 6"/>
        <circle cx="10" cy="20" r="1.8"/><circle cx="19" cy="20" r="1.8"/>
      </svg>
      <span>SHOP NOW</span>
      <svg class="chevron" width="26" height="16" viewBox="0 0 26 16" fill="none" stroke="#fff" stroke-width="4" stroke-linecap="square">
        <path d="M3 3l10 10 10-10"/>
      </svg>
    </div>
  </section>

  <section class="promo-banner banner-two">
    <div class="product-photo photo-dslr" role="img" aria-label="Black DSLR camera with lens and battery grip"></div>
    <h3 class="promo-heading">PHOTOGRAPHY</h3>
    <p class="promo-copy"><span class="lead">L</span>orem ipsum dolor sit amet, con-<br>sectetur adipiscing elit, sed do<br>eiusmod tempor incididunt ut<br>labore et dolore magna aliqua.</p>
    <div class="shop-button">
      <svg width="26" height="24" viewBox="0 0 26 24" fill="none" stroke="#fff" stroke-width="2" stroke-linejoin="round" stroke-linecap="round">
        <path d="M1 2h4l3 13h13l3-9H6.5"/>
        <path d="M9 7.5l1.5 6M13 7.5v6M17 7.5l-1.2 6"/>
        <circle cx="10" cy="20" r="1.8"/><circle cx="19" cy="20" r="1.8"/>
      </svg>
      <span>SHOP NOW</span>
      <svg class="chevron" width="26" height="16" viewBox="0 0 26 16" fill="none" stroke="#fff" stroke-width="4" stroke-linecap="square">
        <path d="M3 3l10 10 10-10"/>
      </svg>
    </div>
  </section>

  <footer class="footer-band"></footer>
</body>
</html>
```